Want to incorporate elements of all these items to make an amazing sign to welcome people to the community. The sign is 6x4 and needs to incorporate the following items:

Welcome to Thistle Grove

Come visit the DWR sales center at 548 marlow road
High Speed Fiber Internet
Land financing starting at $299 (No credit checks)
Let us build your dream home!
517-384-2296
We like the gold and black design no teal or blue that was another agents design. Some combination of the current sign all the stuff listed above and then design elements that tie into the truck wrap.

Target Market(s)

People visiting the neighborhood

Industry/Entity Type

real estate and construction

Font styles to use
Serif

Colors

Designer to choose colors to be used in the design.

Requirements
Must have
• DWR Home Builders Welcomes you to Thistle Grove, Let us build your dream home, Phone number, Land financing starting at $299 NO credit checks

```html
<!DOCTYPE html>
<html lang="en">
<head>
<meta charset="utf-8">
<title>Thistle Grove – Welcome Sign</title>
<link rel="stylesheet" href="https://fonts.googleapis.com/css2?family=Abril+Fatface&family=Bodoni+Moda:wght@700;800&family=Oranienbaum&family=Mr+Dafoe&family=Merriweather:wght@700;900&family=Libre+Baskerville:ital@1&family=Noto+Serif:wght@700&display=swap">
<style>
  :root {
    --page: #ecebe6;
    --black: #050505;
    --gold-deep: #d79e1e;
    --gold-bright: #f6c71a;
    --gold-text: #e5ad2a;
    --red-top: #f7a3a3;
    --red: #e3161f;
    --red-deep: #c10f17;
    --white: #ffffff;
    --glow: #5a2a0c;
  }
  html, body {
    margin: 0;
    width: 1174px;
    height: 1200px;
    overflow: hidden;
    background: var(--page);
  }
  .sign {
    position: absolute;
    left: 32px;
    top: 230px;
    width: 1110px;
    height: 739px;
    display: block;
    box-shadow: 0 10px 30px rgba(0,0,0,.25);
  }
  .welcome { font-family: "Abril Fatface", serif; fill: var(--black); }
  .community-name { font-family: "Abril Fatface", serif; fill: var(--black); }
  .community-script { font-family: "Mr Dafoe", cursive; fill: var(--black); }
  .headline { font-family: "Bodoni Moda", serif; font-weight: 800; }
  .headline-white { fill: var(--white); }
  .headline-gold { fill: var(--gold-text); }
  .financing { font-family: "Merriweather", serif; font-weight: 900; fill: var(--white); }
  .price { font-family: "Merriweather", serif; font-weight: 700; fill: var(--black); }
  .credit-note { font-family: "Merriweather", serif; font-weight: 700; fill: var(--white); }
  .visit { font-family: "Oranienbaum", serif; fill: var(--white); }
  .visit-address { font-family: "Bodoni Moda", serif; font-weight: 700; fill: var(--gold-text); }
  .tagline { font-family: "Libre Baskerville", serif; font-style: italic; fill: var(--white); }
  .phone-number { font-family: "Noto Serif", serif; font-weight: 700; fill: var(--white); }
</style>
</head>
<body>
<svg class="sign" viewBox="0 0 1410 939" xmlns="http://www.w3.org/2000/svg" aria-label="Thistle Grove welcome sign">
  <defs>
    <linearGradient id="goldBand" x1="0" y1="0" x2="1" y2="0">
      <stop offset="0" stop-color="var(--gold-deep)"/>
      <stop offset="0.55" stop-color="var(--gold-bright)"/>
      <stop offset="1" stop-color="var(--gold-bright)"/>
    </linearGradient>
    <linearGradient id="redBar" x1="0" y1="0" x2="0" y2="1">
      <stop offset="0" stop-color="var(--red-top)"/>
      <stop offset="0.35" stop-color="var(--red)"/>
      <stop offset="1" stop-color="var(--red-deep)"/>
    </linearGradient>
    <linearGradient id="goldPill" x1="0" y1="0" x2="1" y2="1">
      <stop offset="0" stop-color="var(--gold-bright)"/>
      <stop offset="1" stop-color="var(--gold-deep)"/>
    </linearGradient>
    <radialGradient id="bottomGlow" cx="0.5" cy="1" r="0.6" fx="0.5" fy="1">
      <stop offset="0" stop-color="var(--glow)" stop-opacity="0.9"/>
      <stop offset="1" stop-color="var(--glow)" stop-opacity="0"/>
    </radialGradient>
  </defs>

  <!-- board -->
  <rect class="board" width="1410" height="939" fill="var(--black)"/>
  <rect class="board-glow" x="0" y="820" width="1410" height="119" fill="url(#bottomGlow)"/>

  <!-- header band -->
  <path class="header-band" d="M0 0 H1410 V225 Q705 395 0 225 Z" fill="url(#goldBand)"/>
  <text class="welcome" x="290" y="110" font-size="64" textLength="445" lengthAdjust="spacingAndGlyphs">Welcome to</text>
  <text class="community-name" x="160" y="235" font-size="160" textLength="690" lengthAdjust="spacingAndGlyphs">Thistle</text>
  <text class="community-script" x="885" y="228" font-size="200" textLength="395" lengthAdjust="spacingAndGlyphs">Grove</text>

  <!-- signal icon -->
  <g class="signal-icon" fill="none" stroke="var(--white)" stroke-linecap="round">
    <path d="M608 352 A58 58 0 0 1 686 352" stroke-width="11"/>
    <path d="M622 369 A36 36 0 0 1 672 369" stroke-width="10"/>
    <path d="M634 384 A16 16 0 0 1 660 384" stroke-width="9"/>
  </g>
  <line x1="647" y1="400" x2="692" y2="368" stroke="var(--red)" stroke-width="5"/>
  <circle cx="647" cy="400" r="9" fill="var(--red)"/>

  <!-- headline -->
  <text class="headline headline-white" x="100" y="468" font-size="100" textLength="235" lengthAdjust="spacingAndGlyphs">HIGH</text>
  <text class="headline headline-gold" x="363" y="468" font-size="100" textLength="278" lengthAdjust="spacingAndGlyphs">SPEED</text>
  <text class="headline headline-white" x="667" y="468" font-size="100" textLength="643" lengthAdjust="spacingAndGlyphs">FIBER INTERNET</text>

  <!-- financing bar -->
  <rect class="financing-bar" x="128" y="503" width="880" height="74" rx="37" fill="url(#redBar)"/>
  <text class="financing" x="180" y="563" font-size="60" textLength="762" lengthAdjust="spacingAndGlyphs">Land financing starting at</text>
  <rect class="price-pill" x="960" y="487" width="165" height="107" rx="32" fill="url(#goldPill)"/>
  <text class="price" x="1042" y="567" font-size="70" text-anchor="middle" textLength="142" lengthAdjust="spacingAndGlyphs">$299</text>

  <g class="credit-bracket" fill="none" stroke="var(--white)" stroke-width="4">
    <path d="M1172 503 H1162 V582 H1172"/>
    <path d="M1270 503 H1280 V582 H1270"/>
  </g>
  <text class="credit-note" font-size="25">
    <tspan x="1177" y="527">No</tspan>
    <tspan x="1177" y="552">credit</tspan>
    <tspan x="1177" y="577">checks</tspan>
  </text>

  <!-- visit -->
  <path class="pin-icon" d="M348 696 C330 670 325 660 325 646 A23 23 0 0 1 371 646 C371 660 366 670 348 696 Z" fill="var(--gold-text)"/>
  <circle cx="348" cy="645" r="9" fill="var(--black)"/>
  <text class="visit" x="388" y="690" font-size="60" textLength="635" lengthAdjust="spacingAndGlyphs">COME VISIT THE DWR SALES</text>
  <line x1="173" y1="728" x2="280" y2="728" stroke="var(--white)" stroke-width="7"/>
  <line x1="1135" y1="728" x2="1240" y2="728" stroke="var(--white)" stroke-width="7"/>
  <text class="visit" x="302" y="755" font-size="60" textLength="255" lengthAdjust="spacingAndGlyphs">CENTER AT</text>
  <text class="visit-address" x="573" y="755" font-size="58" textLength="534" lengthAdjust="spacingAndGlyphs">548 MARLOW ROAD</text>

  <!-- tagline & phone -->
  <line x1="66" y1="820" x2="642" y2="820" stroke="var(--white)" stroke-width="2"/>
  <line x1="66" y1="895" x2="642" y2="895" stroke="var(--white)" stroke-width="3"/>
  <text class="tagline" x="66" y="870" font-size="44" textLength="576" lengthAdjust="spacingAndGlyphs">Let us build your dream home!</text>

  <circle class="phone-icon" cx="722" cy="856" r="42" fill="none" stroke="var(--white)" stroke-width="3"/>
  <path d="M702 838 l10 -8 l9 14 l-6 6 q4 12 16 17 l6 -6 l14 9 l-8 10 q-34 -6 -41 -42 z" fill="var(--gold-text)"/>
  <g fill="none" stroke="var(--gold-text)" stroke-width="3" stroke-linecap="round">
    <path d="M728 838 a14 14 0 0 1 12 12"/>
    <path d="M730 828 a24 24 0 0 1 20 20"/>
  </g>
  <text class="phone-number" x="792" y="891" font-size="106" textLength="555" lengthAdjust="spacingAndGlyphs">517-384-2296</text>
</svg>
</body>
</html>
```